Ultra Distance Charity Bike Ride.

Hello.

I need a business card to pass to people whilst out on my charity bike ride.

I’m raising funds/awareness about mental health. My funds are going to Open Harbour. I have a link to my donation page in my instagram bio. My instagram page will also be a source for people to follow my adventures. My Instagram page is tomwillet.

I would like to have this card not for just one trip, I’d like it to be something that I can use on future endeavors.

```html
<!DOCTYPE html>
<html lang="en">
<head>
<meta charset="utf-8">
<title>Tom Willet – Charity Bike Ride Card</title>
<link rel="stylesheet" href="https://fonts.googleapis.com/css2?family=Open+Sans:wght@400;600;700&display=swap">
<style>
  :root {
    --bg-light: #a4aaa9;
    --bg-dark: #4f5553;
    --card: #ffffff;
    --teal: #1b8ab3;
    --teal-deep: #17789c;
    --orange: #fbb017;
    --orange-deep: #f7941d;
    --ink: #3a3a3a;
  }
  * { box-sizing: border-box; margin: 0; padding: 0; }
  html, body { width: 1200px; height: 900px; overflow: hidden; }
  body {
    background: radial-gradient(ellipse at 45% 40%, var(--bg-light) 0%, #8c9391 55%, var(--bg-dark) 100%);
    font-family: "Open Sans", sans-serif;
    position: relative;
  }
  .card {
    position: absolute;
    left: 320px;
    width: 560px;
    height: 320px;
    background: var(--card);
    box-shadow: 0 18px 40px rgba(0,0,0,0.28);
    overflow: hidden;
  }
  .card--front { top: 100px; }
  .card--back { top: 480px; }

  /* Front */
  .brand {
    position: absolute;
    top: 92px;
    left: 0; right: 0;
    display: flex;
    align-items: center;
    justify-content: center;
    gap: 14px;
  }
  .brand__dot {
    width: 34px; height: 34px;
    border-radius: 50%;
    background: var(--orange);
  }
  .brand__name {
    font-size: 40px;
    font-weight: 400;
    color: var(--teal);
    letter-spacing: 0.5px;
  }
  .front-tagline {
    position: absolute;
    top: 158px; left: 0; right: 0;
    text-align: center;
    font-size: 15px;
    color: var(--ink);
  }
  .front-band {
    position: absolute;
    left: 0; right: 0;
    bottom: 48px;
    height: 52px;
    background: linear-gradient(90deg, var(--orange) 0%, var(--orange) 70%, var(--orange-deep) 100%);
    display: flex;
    align-items: center;
    justify-content: center;
    color: #fff;
    font-size: 17px;
    letter-spacing: 1.5px;
  }

  /* Back */
  .back-panel { position: absolute; inset: 0; }
  .back-brand {
    position: absolute;
    top: 40px; left: 40px;
    display: flex; align-items: center; gap: 8px;
  }
  .back-brand .brand__dot { width: 18px; height: 18px; }
  .back-brand .brand__name { font-size: 22px; }
  .contact-list {
    position: absolute;
    top: 110px; left: 40px;
    list-style: none;
  }
  .contact-list li {
    display: flex; align-items: center; gap: 12px;
    font-size: 15px;
    color: var(--ink);
    height: 30px;
  }
  .contact-list svg { width: 16px; height: 16px; fill: var(--teal); flex: none; }
  .ribbon {
    position: absolute;
    top: 128px; left: 320px;
    width: 200px; height: 62px;
    background: var(--orange);
    color: #fff;
    text-align: center;
    padding-top: 8px;
    box-shadow: 0 4px 8px rgba(0,0,0,0.15);
  }
  .ribbon__name { font-size: 20px; font-weight: 700; line-height: 1.1; letter-spacing: 0.5px; }
  .ribbon__role { font-size: 14px; line-height: 1.3; }
</style>
</head>
<body>

<section class="card card--front" aria-label="Card front">
  <div class="brand">
    <span class="brand__dot"></span>
    <span class="brand__name">tomwillet</span>
  </div>
  <p class="front-tagline">Riding for mental health · Supporting Open Harbour</p>
  <div class="front-band">ULTRA DISTANCE CHARITY BIKE RIDE</div>
</section>

<section class="card card--back" aria-label="Card back">
  <svg class="back-panel" viewBox="0 0 560 320" preserveAspectRatio="none">
    <path d="M370 0 C 340 110, 340 210, 375 320 L560 320 L560 0 Z" fill="var(--orange)"/>
    <path d="M378 0 C 348 110, 348 210, 383 320 L560 320 L560 0 Z" fill="var(--teal)"/>
    <path d="M480 320 L560 240 L560 320 Z" fill="var(--teal-deep)"/>
  </svg>

  <div class="back-brand">
    <span class="brand__dot"></span>
    <span class="brand__name">tomwillet</span>
  </div>

  <ul class="contact-list">
    <li>
      <svg viewBox="0 0 24 24"><circle cx="12" cy="12" r="10"/></svg>
      Follow: @tomwillet
    </li>
    <li>
      <svg viewBox="0 0 24 24"><path d="M12 21 3.5 12.5A5 5 0 0 1 12 6a5 5 0 0 1 8.5 6.5z"/></svg>
      Donate via the link in my bio
    </li>
    <li>
      <svg viewBox="0 0 24 24"><path d="M5 12h11M12 6l6 6-6 6" stroke="var(--teal)" stroke-width="3" fill="none"/></svg>
      Funds go to Open Harbour
    </li>
    <li>
      <svg viewBox="0 0 24 24"><path d="M12 3 2 12h3v9h5v-6h4v6h5v-9h3z"/></svg>
      www.openharbour.org
    </li>
  </ul>

  <div class="ribbon">
    <div class="ribbon__name">TOM WILLET</div>
    <div class="ribbon__role">Charity Rider</div>
  </div>
</section>

</body>
</html>
```